Harrowgate Supply Group Business Card Design

The Business Card will be one side only with Harrowgate Supplies Group Logo
Card should have:
Name
Title
Office phone Number
Cell Number
email address
Website
Street Address
Our Slogan is Rugged and Reliable
Looking for something that stands out from other business cards

Target Market(s)

Heavy equipment Lease Company

```html
<!DOCTYPE html>
<html lang="en">
<head>
<meta charset="utf-8">
<title>Harrowgate Supply Group – Business Card</title>
<link href="https://fonts.googleapis.com/css2?family=Montserrat:wght@300;400;500;700&display=swap" rel="stylesheet">
<style>
  :root {
    --navy: #1f1b72;
    --navy-deep: #17145a;
    --red: #d3142c;
    --white: #ffffff;
    --paper: #fbfbfb;
    --ink: #2b2b3a;
    --backdrop: #e6e6e8;
  }
  * { margin: 0; padding: 0; box-sizing: border-box; }
  html, body {
    width: 1200px; height: 1021px; overflow: hidden;
    background: var(--backdrop);
    font-family: "Montserrat", sans-serif;
  }
  .canvas {
    position: relative; width: 1200px; height: 1021px;
  }
  .card {
    position: absolute; left: 250px; width: 700px; height: 400px;
    box-shadow: 0 10px 30px rgba(0,0,0,0.18);
  }
  .card-front { top: 70px; background: var(--navy); color: var(--white); }
  .card-back { top: 550px; background: var(--paper); }

  .front-brand {
    position: absolute; left: 0; right: 0; top: 160px;
    display: flex; align-items: center; justify-content: center; gap: 16px;
  }
  .brand-dot { width: 22px; height: 22px; border-radius: 50%; background: var(--red); }
  .front-name {
    font-size: 28px; font-weight: 700; letter-spacing: 0.5px;
    text-transform: uppercase; color: var(--white);
  }
  .slogan {
    position: absolute; left: 0; right: 0; top: 240px; text-align: center;
    font-size: 15px; font-weight: 500; letter-spacing: 1px; color: var(--white);
  }

  .back-brand {
    position: absolute; right: 48px; top: 52px;
    display: flex; align-items: center; gap: 10px;
  }
  .back-brand .brand-dot { width: 16px; height: 16px; background: var(--navy); }
  .back-name {
    font-size: 17px; font-weight: 700; text-transform: uppercase; color: var(--red);
  }

  .identity { position: absolute; left: 60px; top: 150px; }
  .person { font-size: 30px; color: var(--navy); line-height: 1; }
  .person .first { font-weight: 300; }
  .person .last { font-weight: 700; }
  .job-title {
    margin-top: 6px; font-size: 17px; font-weight: 400; color: var(--red); letter-spacing: 0.5px;
  }
  .title-rule { margin-top: 10px; width: 60px; height: 3px; background: var(--red); }

  .contacts { position: absolute; left: 60px; top: 262px; list-style: none; }
  .contacts li {
    display: flex; align-items: center; gap: 12px;
    font-size: 14px; color: var(--ink); height: 22px;
  }
  .contacts li.address { margin-top: 8px; }
  .contacts svg { width: 14px; height: 14px; flex: none; }
</style>
</head>
<body>
<div class="canvas">

  <section class="card card-front">
    <div class="front-brand">
      <span class="brand-dot"></span>
      <span class="front-name">Harrowgate Supplies Group</span>
    </div>
    <p class="slogan">RUGGED AND RELIABLE</p>
  </section>

  <section class="card card-back">
    <div class="back-brand">
      <span class="brand-dot"></span>
      <span class="back-name">Harrowgate Supplies Group</span>
    </div>

    <div class="identity">
      <p class="person"><span class="first">YOUR </span><span class="last">NAME</span></p>
      <p class="job-title">JOB TITLE</p>
      <div class="title-rule"></div>
    </div>

    <ul class="contacts">
      <li>
        <svg viewBox="0 0 16 16"><path fill="#1f1b72" d="M2 5c0-2 2-3 6-3s6 1 6 3v1h-3V5H5v1H2z M4 7h8l2 6H2z"/></svg>
        000 000 0000
      </li>
      <li>
        <svg viewBox="0 0 16 16"><rect x="4" y="1" width="8" height="14" rx="1.5" fill="none" stroke="#1f1b72" stroke-width="1.6"/><circle cx="8" cy="12.5" r="0.9" fill="#1f1b72"/></svg>
        000 000 0000
      </li>
      <li>
        <svg viewBox="0 0 16 16"><rect x="1" y="3" width="14" height="10" fill="#1f1b72"/><path d="M1 3l7 6 7-6" fill="none" stroke="#fff" stroke-width="1.2"/></svg>
        youremail@xyz.com
      </li>
      <li>
        <svg viewBox="0 0 16 16" fill="none" stroke="#1f1b72" stroke-width="1.2"><circle cx="8" cy="8" r="6.5"/><ellipse cx="8" cy="8" rx="3" ry="6.5"/><path d="M1.5 8h13M2.5 4.8h11M2.5 11.2h11"/></svg>
        www.yourwebsite.com
      </li>
      <li class="address">
        <svg viewBox="0 0 16 16"><path fill="#d3142c" d="M8 1a5 5 0 0 0-5 5c0 4 5 9 5 9s5-5 5-9a5 5 0 0 0-5-5z"/><circle cx="8" cy="6" r="1.8" fill="#fff"/></svg>
        0000, Street Name, City, ST 00000
      </li>
    </ul>
  </section>

</div>
</body>
</html>
```